Re-branding stationary for Company

Orvane Diamonds is a diamond trading company that has been established since more then 30years.

We are currently looking to re-design our current logo design into something more modern and more appealing the the new generation. Small changes are what we are looking for that will give our company a little more modern look and a new appeal.
The design should be on similar lines to what our current logo is, but we are definitely wanting to have some modern changes to this.
Along with this, we are looking to have design for complete stationary including, business cards, envelopes, letterheads, etc..

Attached is our current logo, can use this as a base point towards creating a new design.
Updates

Project Deadline Extended Reason: Am still looking for wonderful and amazingly creative design for my company, a facelift with a little modern touchHave provided you with a current logo of the company as inspiration to make something new and unique. PLEASE DO NOT USE COPY THE LOGO FILE AS IT IS! Added Wednesday, May 6, 2015

Target Market(s)

We are a company established since over 30 years, and want to maintain our core fundamental values which is portrayed through our logo. Use this as a base into creating new modern design.

Industry/Entity Type

It Company

Font styles to use
Serif
Sans Serif
Decorative
Script

Requirements
Must have
• A modern touch
• Color combination should be similar in terms with what we currently use in attached design.
Nice to have
• Want that the design is appealing using simple but yet modern features to change and restructure the current company logo.
Should not have
• Not looking more multi colored design
• Not gotta be too overly extravagant

```html
<!DOCTYPE html>
<html lang="en">
<head>
<meta charset="utf-8">
<title>Orvane Diamonds – Stationery</title>
<link rel="stylesheet" href="https://fonts.googleapis.com/css2?family=Bodoni+Moda:ital,wght@0,400;0,500;0,700&display=swap">
<style>
:root{
  --gold-dark:#9b7a3f;
  --gold-light:#e2bf63;
  --ink:#0d0d0d;
  --panel-grey:#6d6e70;
  --stage:#ebebeb;
  --paper:#ffffff;
  --text:#1a1a1a;
  --muted:#cfcfcf;
  --serif:"Bodoni Moda", "Times New Roman", serif;
}
*{margin:0;padding:0;box-sizing:border-box}
html,body{width:1200px;height:726px;overflow:hidden;background:var(--stage);font-family:var(--serif)}
.canvas{position:relative;width:1200px;height:726px;overflow:hidden;background:var(--stage)}

/* brand guide panel */
.guide{position:absolute;left:0;top:0;width:232px;height:726px;background:var(--panel-grey);color:#fff}
.guide-logo{height:117px;display:flex;flex-direction:column;align-items:center;justify-content:center;text-align:center}
.guide-logo--dark{background:var(--ink)}
.guide-logo--light{background:var(--paper)}
.wordmark{color:var(--gold-dark);font-weight:500;letter-spacing:.5px;display:flex;align-items:center;gap:6px}
.wordmark .dot{width:7px;height:7px;border-radius:50%;background:var(--gold-dark)}
.guide-logo .wordmark{font-size:15px}
.guide-logo--dark .wordmark{color:var(--gold-light)}
.guide-logo--dark .wordmark .dot{background:var(--gold-light)}
.tagline{font-size:7px;color:var(--gold-dark);margin-top:2px}
.guide-logo--dark .tagline{color:var(--gold-light)}
.guide-heading{text-align:center;font-size:18px;margin-top:10px}
.swatches{display:flex;gap:8px;justify-content:center;margin-top:4px}
.swatch{width:40px}
.swatch-chip{height:40px}
.swatch-chip--dark{background:var(--gold-dark)}
.swatch-chip--light{background:var(--gold-light)}
.swatch-chip--ink{background:var(--ink)}
.swatch-code{font-size:4px;line-height:5px;color:#e5e5e5;margin-top:3px}
.font-sample{text-align:center;margin-top:6px}
.font-sample .name{font-size:14px;letter-spacing:.5px}
.font-sample .sub{font-size:8px;margin-bottom:14px}
.font-sample .face{font-size:19px;line-height:22px}
.font-sample .alphabet{font-size:17px;line-height:19px}
.pangrams{text-align:center;margin-top:16px;line-height:16px}
.pangrams p:nth-child(1){font-size:7px}
.pangrams p:nth-child(2){font-size:8px}
.pangrams p:nth-child(3){font-size:9px}
.pangrams p:nth-child(4){font-size:10px}

/* letterhead */
.letterhead{position:absolute;left:282px;top:48px;width:430px;height:620px;background:var(--paper);box-shadow:0 1px 3px rgba(0,0,0,.12)}
.letterhead-brand{position:absolute;right:38px;top:38px;text-align:center}
.letterhead-brand .wordmark{font-size:12px}
.letterhead-brand .tagline{font-size:6px}
.letter-body{position:absolute;left:48px;top:118px;width:330px;font-size:8px;line-height:10.5px;color:var(--text)}
.letter-body .salutation{font-weight:700;margin-bottom:12px}
.letter-body p{margin-bottom:11px;text-align:justify}
.letter-body .signoff{margin-top:4px}
.letter-body .signatory{font-weight:700;margin-top:26px}
.letterhead-footer{position:absolute;left:0;bottom:0;width:100%;height:40px;background:var(--ink)}
.letterhead-contact{position:absolute;left:48px;bottom:52px;font-size:6px;line-height:9px;font-weight:700;color:var(--text)}
.letterhead-footer-brand{position:absolute;right:38px;bottom:56px;text-align:center}
.letterhead-footer-brand .wordmark{font-size:10px}
.letterhead-footer-brand .tagline{font-size:5px}

/* envelopes */
.envelope{position:absolute;left:760px;width:400px;height:196px;background:var(--ink);overflow:hidden}
.envelope--front{top:48px}
.envelope--back{top:272px}
.envelope-brand{position:absolute;left:22px;top:24px;text-align:center}
.envelope-brand .wordmark,.envelope-back-brand .wordmark{font-size:11px;color:var(--gold-light)}
.envelope-brand .wordmark .dot,.envelope-back-brand .wordmark .dot{background:var(--gold-light)}
.envelope-brand .tagline,.envelope-back-brand .tagline{font-size:5px;color:var(--gold-light)}
.envelope-address{position:absolute;right:36px;top:30px;font-size:5.5px;line-height:8px;color:var(--gold-light)}
.envelope-flap{position:absolute;inset:0}
.envelope-back-brand{position:absolute;left:0;right:0;top:128px;display:flex;flex-direction:column;align-items:center}

/* business cards */
.card{position:absolute;top:500px;width:190px;height:108px;background:var(--ink);overflow:hidden}
.card--front{left:760px;display:flex;flex-direction:column;align-items:center;justify-content:center}
.card--front .wordmark{font-size:11px;color:var(--gold-light)}
.card--front .wordmark .dot{background:var(--gold-light)}
.card--front .tagline{font-size:5px;color:var(--gold-light)}
.card--back{left:970px}
.card-facets{position:absolute;right:0;top:0;width:110px;height:108px;background:linear-gradient(135deg,#1c1c1c 0%,#2a2a2a 45%,#111 100%)}
.card-contact{position:absolute;left:14px;top:40px;font-size:5px;line-height:8px;color:var(--gold-light)}
.card-person{position:absolute;left:120px;top:22px;color:var(--gold-light)}
.card-person .person-name{font-size:10px}
.card-person .person-role{font-size:5px}
</style>
</head>
<body>
<div class="canvas">

  <aside class="guide">
    <div class="guide-logo guide-logo--dark">
      <div class="wordmark"><span class="dot"></span>ORVANE DIAMONDS</div>
      <div class="tagline">import-export of rough-polished</div>
    </div>
    <div class="guide-logo guide-logo--light">
      <div class="wordmark"><span class="dot"></span>ORVANE DIAMONDS</div>
      <div class="tagline">import-export of rough-polished</div>
    </div>

    <h2 class="guide-heading">color</h2>
    <div class="swatches">
      <div class="swatch"><div class="swatch-chip swatch-chip--dark"></div>
        <div class="swatch-code">C 37 M 49 Y 86 K 16<br>R 160 G 118 B 61<br>#A0763D</div></div>
      <div class="swatch"><div class="swatch-chip swatch-chip--light"></div>
        <div class="swatch-code">C 15 M 24 Y 71 K 0<br>R 222 G 187 B 96<br>#DEBB60</div></div>
      <div class="swatch"><div class="swatch-chip swatch-chip--ink"></div>
        <div class="swatch-code">C 75 M 67 Y 66 K 90<br>R 0 G 0 B 0<br>#000000</div></div>
    </div>

    <h2 class="guide-heading">font</h2>
    <div class="font-sample">
      <div class="name">ORVANE DIAMONDS</div>
      <div class="sub">import-export of rough-polished</div>
      <div class="face">Bodoni MT</div>
      <div class="alphabet">abcdefghijk<br>lmnopqrstu<br>vwxyz<br>1234567890</div>
    </div>
    <div class="pangrams">
      <p>The quick brown fox jumps over the lazy dog</p>
      <p>The quick brown fox jumps over the lazy dog</p>
      <p>The quick brown fox jumps over the lazy dog</p>
      <p>The quick brown fox jumps over the lazy dog</p>
    </div>
  </aside>

  <section class="letterhead">
    <div class="letterhead-brand">
      <div class="wordmark"><span class="dot"></span>ORVANE DIAMONDS</div>
      <div class="tagline">import-export of rough-polished</div>
    </div>
    <div class="letter-body">
      <p class="salutation">DEAR CLIENT</p>
      <p>Lorem ipsum dolor sit amet, consectetuer adipiscing elit, sed diam nonummy nibh euismod tincidunt ut laoreet dolore magna aliquam erat volutpat. Ut wisi enim ad minim veniam, quis nostrud exerci tation ullamcorper suscipit lobortis nisl ut aliquip ex ea commodo consequat.</p>
      <p>Duis autem vel eum iriure dolor in hendrerit in vulputate velit esse molestie consequat, vel illum dolore eu feugiat nulla facilisis at vero eros et accumsan et iusto odio dignissim qui blandit praesent luptatum zzril delenit augue duis dolore te feugait nulla facilisi.</p>
      <p>Vel illum dolore eu feugiat nulla facilisis at vero eros et accumsan et iusto odio dignissim qui blandit praesent luptatum. Nam liber tempor cum soluta nobis eleifend option congue nihil imperdiet doming id quod mazim placerat.</p>
      <p class="signoff">Yours sincerely.</p>
      <p class="signatory">OWNER</p>
    </div>
    <div class="letterhead-contact">Vel illum dolore eu feugiat<br>01 555 0142<br>Street Vel illum dolore No. 12</div>
    <div class="letterhead-footer-brand">
      <div class="wordmark"><span class="dot"></span>ORVANE DIAMONDS</div>
      <div class="tagline">import-export of rough-polished</div>
    </div>
    <div class="letterhead-footer"></div>
  </section>

  <section class="envelope envelope--front">
    <div class="envelope-brand">
      <div class="wordmark"><span class="dot"></span>ORVANE DIAMONDS</div>
      <div class="tagline">import-export of rough-polished</div>
    </div>
    <div class="envelope-address">Mr. Lorem Ipsum<br>Lorem Ipsum Street 12<br>Lorem Ipsum City<br>PO BOX 123456<br>+31 555 0190</div>
  </section>

  <section class="envelope envelope--back">
    <svg class="envelope-flap" viewBox="0 0 400 196" preserveAspectRatio="none">
      <polyline points="0,0 200,100 400,0" fill="none" stroke="#2b2b2b" stroke-width="1.2"/>
      <polyline points="0,196 150,90" fill="none" stroke="#222" stroke-width="1"/>
      <polyline points="400,196 250,90" fill="none" stroke="#222" stroke-width="1"/>
    </svg>
    <div class="envelope-back-brand">
      <div class="wordmark"><span class="dot"></span>ORVANE DIAMONDS</div>
      <div class="tagline">import-export of rough-polished</div>
    </div>
  </section>

  <section class="card card--front">
    <div class="wordmark"><span class="dot"></span>ORVANE DIAMONDS</div>
    <div class="tagline">import-export of rough-polished</div>
  </section>

  <section class="card card--back">
    <div class="card-facets" role="img" aria-label="Faint faceted diamond pattern in dark greys"></div>
    <div class="card-person">
      <div class="person-name">Elin Marsh</div>
      <div class="person-role">Managing Director</div>
    </div>
    <div class="card-contact">Lorem Ipsum Street 12<br>+31 555 0190<br>info@orvanediamonds.com</div>
  </section>

</div>
</body>
</html>
```